Home based bath & shave business wants to redesign labels

I would like to have new labels designed to fit the body lotion and bath oil bottles. We want them similar but different. The key ingredient for all of Ferrante's Bath & Shave products is olive oil.

You are free to change colors. I have attached our logo and current labels. The current labels just don't look right to me (pictures attached). I like the script font, but am willing to entertain another. I have our logo in several formats and the font, should you want it.

Target Market(s)

Women

Industry/Entity Type

Business

Font styles to use
Decorative
Script

Requirements
Must have
• Both product labels must include our logo.The logo must stay the same though to make it work with the label, you can change the color if needed.
• It should be a vertical label.
• The bottle used is a 8 oz Clear PET Tapered Naples Oval Bottle (I have attached pictures) and its dimensions are:
• Length 2.548 in / 6.472 cm
• Width 1.479 in / 3.757 cm
• Height 6.639 in / 16.863 cm

```html
<!DOCTYPE html>
<html lang="en">
<head>
<meta charset="utf-8">
<title>Ferrante's Bath &amp; Shave – Body Lotion and Bath Oil Labels</title>
<link rel="stylesheet" href="https://fonts.googleapis.com/css2?family=Oswald:wght@200;300;500&display=swap">
<style>
  :root {
    --bg: #ffffff;
    --cap: #0b1117;
    --lotion-bottle: #f2eedf;
    --lotion-bottle-edge: #e6e0c9;
    --lotion-label: #e89bb5;
    --oil-bottle: #f4e11a;
    --oil-bottle-edge: #dcc21a;
    --oil-label: #fbf8da;
    --oil-accent: #dcc52a;
    --cream-line: #fbf6dc;
    --ink: #1f1f1f;
    --sprig-lotion: #f6d5df;
    --sprig-oil: #efe39a;
  }
  * { margin: 0; padding: 0; box-sizing: border-box; }
  html, body { width: 1200px; height: 1000px; overflow: hidden; background: var(--bg); }
  .canvas { position: relative; width: 1200px; height: 1000px; }
  .bottles { position: absolute; inset: 0; }
  .label-text { position: absolute; width: 130px; text-align: center; color: var(--ink);
    font-family: "Oswald", sans-serif; }
  .brand { position: absolute; top: 412px; width: 130px; text-align: center;
    font-family: "Oswald", sans-serif; font-weight: 500; font-size: 14px; letter-spacing: .5px; }
  .brand--lotion { left: 353px; color: #5a3a2a; }
  .brand--oil { left: 743px; color: #7a6412; }
  .product-name { top: 452px; font-weight: 200; font-size: 40px; line-height: 44px; }
  .claim { top: 684px; font-weight: 300; font-size: 13.5px; line-height: 17px; letter-spacing: .5px; }
  .claim::before, .claim::after { content: ""; display: block; height: 1px; background: var(--ink);
    width: 104px; margin: 0 auto; }
  .claim::before { margin-bottom: 5px; }
  .claim::after { margin-top: 6px; }
  .ingredients { top: 754px; font-weight: 300; font-size: 9px; line-height: 12.3px; }
  .col-lotion { left: 353px; }
  .col-oil { left: 743px; }
</style>
</head>
<body>
<main class="canvas">
  <svg class="bottles" width="1200" height="1000" viewBox="0 0 1200 1000" xmlns="http://www.w3.org/2000/svg">
    <defs>
      <linearGradient id="lotion-body" x1="0" x2="1">
        <stop offset="0" stop-color="var(--lotion-bottle-edge)"/>
        <stop offset=".3" stop-color="var(--lotion-bottle)"/>
        <stop offset=".8" stop-color="var(--lotion-bottle)"/>
        <stop offset="1" stop-color="var(--lotion-bottle-edge)"/>
      </linearGradient>
      <linearGradient id="oil-body" x1="0" x2="1">
        <stop offset="0" stop-color="var(--oil-bottle-edge)"/>
        <stop offset=".3" stop-color="var(--oil-bottle)"/>
        <stop offset=".8" stop-color="var(--oil-bottle)"/>
        <stop offset="1" stop-color="var(--oil-bottle-edge)"/>
      </linearGradient>
      <path id="bottle-shape" d="M335,235 L475,235 C478,270 500,290 535,310 C565,328 572,350 572,390 L530,966 Q528,978 505,978 L305,978 Q284,978 282,966 L240,390 C240,350 248,328 278,310 C312,290 332,270 335,235 Z"/>
      <path id="label-shape" d="M318,420 C340,385 420,360 487,333 C505,380 505,470 485,560 C470,640 485,720 470,830 C462,870 440,880 420,885 C395,888 380,900 365,908 C350,860 340,780 332,720 C328,680 345,650 370,610 C385,580 370,540 345,490 C330,460 318,440 318,420 Z"/>
      <path id="label-swoosh" d="M336,414 C380,390 430,372 477,350 C488,420 482,500 470,570 C455,650 472,740 458,830 C452,860 430,872 400,882"/>
      <path id="label-outer-band" d="M306,428 C310,470 340,520 358,560 C372,595 352,625 330,660 C312,690 318,730 325,770"/>
      <g id="cap">
        <rect x="335" y="118" width="140" height="117"/>
        <rect x="346" y="2" width="118" height="30" rx="15"/>
        <rect x="346" y="30" width="118" height="30" rx="15"/>
        <rect x="346" y="58" width="118" height="30" rx="15"/>
        <rect x="346" y="86" width="118" height="34" rx="15"/>
      </g>
    </defs>

    <g class="bottle bottle--lotion">
      <use href="#bottle-shape" fill="url(#lotion-body)"/>
      <use href="#cap" fill="var(--cap)"/>
      <use href="#label-outer-band" fill="none" stroke="var(--lotion-label)" stroke-width="7"/>
      <use href="#label-shape" fill="var(--lotion-label)"/>
      <use href="#label-swoosh" fill="none" stroke="var(--cream-line)" stroke-width="7"/>
      <circle cx="418" cy="405" r="5" fill="#5a3a2a"/>
      <rect role="img" aria-label="Olive sprig illustration" x="370" y="540" width="92" height="92" rx="40" fill="var(--sprig-lotion)" opacity=".85"/>
    </g>

    <g class="bottle bottle--oil" transform="translate(390 0)">
      <use href="#bottle-shape" fill="url(#oil-body)"/>
      <use href="#cap" fill="var(--cap)"/>
      <use href="#label-outer-band" fill="none" stroke="var(--oil-label)" stroke-width="7"/>
      <use href="#label-shape" fill="var(--oil-label)"/>
      <use href="#label-swoosh" fill="none" stroke="var(--oil-accent)" stroke-width="7"/>
      <circle cx="418" cy="405" r="5" fill="#7a6412"/>
      <rect role="img" aria-label="Olive sprig illustration" x="370" y="540" width="92" height="92" rx="40" fill="var(--sprig-oil)" opacity=".85"/>
    </g>
  </svg>

  <div class="brand brand--lotion">FERRANTE'S</div>
  <div class="label-text product-name col-lotion">BODY<br>LOTION</div>
  <div class="label-text claim col-lotion">NOURISHED<br>WITH<br>OLIVE OIL</div>
  <p class="label-text ingredients col-lotion">INGREDIENTS: Water,<br>Olive Oil, Aloe Vera Juice,<br>Avocado Oil, Rice Bran Oil,<br>BTMS-50, Glycerin, Stearyl<br>Alcohol, Oat Extract,<br>DL Panthenol, Optiphen,<br>Buckthorn Extract,<br>Vitamin-E and<br>Fragrance oil</p>

  <div class="brand brand--oil">FERRANTE'S</div>
  <div class="label-text product-name col-oil">BATH<br>OIL</div>
  <div class="label-text claim col-oil">NOURISHED<br>WITH<br>OLIVE OIL</div>
  <p class="label-text ingredients col-oil">INGREDIENTS: Olive Oil,<br>Grapeseed Oil<br>and Fragrance Oil</p>
</main>
</body>
</html>
```